Logo-Design für Montageunternehmen
Zielgruppe
Montageunternehmen
Gartenhäuser Zäune dunstabzugshauben....
Aufgabenstellung
Es soll auch einfarbig bei einem Siebdruck gut aussehen.
Darf für die Druckversion aber auch einwenig Farbe beinhalten

```html
<!DOCTYPE html>
<html lang="de">
<head>
<meta charset="utf-8">
<title>Tovel Mont Plus – Visitenkarte</title>
<link href="https://fonts.googleapis.com/css2?family=Montserrat:wght@400;600&display=swap" rel="stylesheet">
<style>
  :root {
    --backdrop: #c1c0be;
    --paper: #ffffff;
    --navy: #0a4a6e;
    --lime: #8cc63f;
  }
  * { margin: 0; padding: 0; box-sizing: border-box; }
  html, body { width: 1200px; height: 1176px; overflow: hidden; }
  body {
    background: var(--backdrop);
    font-family: "Montserrat", Arial, sans-serif;
    position: relative;
  }
  .card { position: absolute; width: 723px; height: 458px; }
  .card-front { left: 232px; top: 92px; background: var(--paper); }
  .card-back { left: 237px; top: 644px; background: var(--lime); }

  .wordmark {
    position: absolute;
    color: var(--navy);
    font-weight: 600;
    display: flex;
    align-items: center;
    white-space: nowrap;
  }
  .wordmark .dot {
    display: inline-block;
    background: var(--lime);
    border-radius: 50%;
  }
  .card-front .wordmark { left: 30px; top: 60px; font-size: 44px; gap: 16px; }
  .card-front .wordmark .dot { width: 24px; height: 24px; }

  .company { position: absolute; left: 363px; top: 214px; width: 355px; text-align: center; }
  .company-name { color: var(--navy); font-size: 29px; font-weight: 400; letter-spacing: 0.3px; }
  .tagline {
    color: var(--lime); font-size: 16px; margin-top: 2px;
    display: flex; align-items: center; gap: 8px; justify-content: center;
  }
  .tagline::before, .tagline::after { content: ""; width: 32px; height: 1px; background: var(--lime); }

  .person { position: absolute; left: 25px; top: 262px; }
  .person-name { color: var(--lime); font-size: 29px; font-weight: 400; }
  .address { display: flex; gap: 10px; margin-top: 6px; color: var(--navy); font-size: 18px; line-height: 23px; }
  .address svg { flex: none; margin-top: 2px; }

  .contacts { position: absolute; left: 360px; top: 302px; list-style: none; }
  .contacts li { display: flex; align-items: center; gap: 10px; color: var(--navy); font-size: 18px; height: 24px; margin-bottom: 14px; }
  .contacts svg { flex: none; }

  .accent-bar { position: absolute; right: 0; top: 299px; width: 12px; height: 159px; background: var(--lime); }

  .card-back .wordmark { left: 0; right: 0; top: 170px; justify-content: center; font-size: 52px; gap: 18px; }
  .card-back .wordmark .dot { width: 28px; height: 28px; background: var(--navy); }
  .card-back .tagline-caps {
    position: absolute; left: 0; right: 0; top: 252px; text-align: center;
    color: var(--navy); font-size: 15px; letter-spacing: 3px; font-variant: small-caps; font-weight: 600;
  }
</style>
</head>
<body>
  <section class="card card-front">
    <div class="wordmark"><span class="dot"></span>Tovel Mont Plus</div>

    <div class="company">
      <p class="company-name">Tovel Mont Plus</p>
      <p class="tagline">Montage mit Herz und Verstand</p>
    </div>

    <div class="person">
      <p class="person-name">Ivo Tovel</p>
      <div class="address">
        <svg width="18" height="26" viewBox="0 0 18 26" aria-hidden="true">
          <path d="M9 0C4 0 0 4 0 9c0 6.5 9 17 9 17s9-10.5 9-17C18 4 14 0 9 0z" fill="var(--lime)"/>
          <circle cx="9" cy="9" r="3.5" fill="#fff"/>
        </svg>
        <p>Lindenweg 17<br>91287 Hollfeldern</p>
      </div>
    </div>

    <ul class="contacts">
      <li>
        <svg width="22" height="22" viewBox="0 0 22 22" aria-hidden="true">
          <circle cx="11" cy="11" r="10" fill="none" stroke="var(--lime)" stroke-width="1.6"/>
          <path d="M7.5 6c.6-.5 1.3-.3 1.6.3l.9 1.8c.2.5 0 1-.4 1.3l-.6.4c.5 1.3 1.6 2.4 2.9 2.9l.4-.6c.3-.4.8-.6 1.3-.4l1.8.9c.6.3.8 1 .3 1.6-1 1.2-2.4 1.4-3.8.7-2.1-1-3.9-2.8-4.9-4.9-.7-1.4-.5-2.8.5-4z" fill="var(--lime)"/>
        </svg>
        +49 151 20475318
      </li>
      <li>
        <svg width="24" height="18" viewBox="0 0 24 18" aria-hidden="true">
          <rect x="0" y="0" width="24" height="18" fill="var(--lime)"/>
          <path d="M0 0l12 10L24 0" fill="none" stroke="#fff" stroke-width="1.5"/>
        </svg>
        tovelmontplus@postfach.de
      </li>
      <li>
        <svg width="24" height="24" viewBox="0 0 24 24" aria-hidden="true" fill="none" stroke="var(--lime)" stroke-width="1.5">
          <circle cx="12" cy="12" r="10.5"/>
          <ellipse cx="12" cy="12" rx="4.5" ry="10.5"/>
          <path d="M1.5 12h21M3 7h18M3 17h18M12 1.5v21"/>
        </svg>
        www.tovel-montagen.de
      </li>
    </ul>

    <div class="accent-bar"></div>
  </section>

  <section class="card card-back">
    <div class="wordmark"><span class="dot"></span>Tovel Mont Plus</div>
    <p class="tagline-caps">Montage mit Herz und Verstand</p>
  </section>
</body>
</html>
```